Business card design for Tolbrin Waste

I would like double-sided business cards for myself and my partner that includes our logo and the existing colour scheme. We provide waste and environmental services to customers in the motor-vehicle and engineering industries.

```html
<!DOCTYPE html>
<html lang="en">
<head>
<meta charset="utf-8">
<title>Tolbrin Waste – Business Cards</title>
<link href="https://fonts.googleapis.com/css2?family=Montserrat:wght@400;500;600;700&display=swap" rel="stylesheet">
<style>
  :root {
    --backdrop: #1c1c1c;
    --card-grey: #4a4a4c;
    --card-white: #ffffff;
    --green-deep: #6aa53c;
    --green-bright: #9cca3c;
    --text-light: #ffffff;
    --text-dark: #4a4a4c;
  }
  * { margin: 0; padding: 0; box-sizing: border-box; }
  html, body {
    width: 1200px; height: 900px; overflow: hidden;
    background: var(--backdrop);
    font-family: "Montserrat", sans-serif;
  }
  .canvas { position: relative; width: 1200px; height: 900px; }

  .card {
    position: absolute;
    width: 620px; height: 354px;
    border-radius: 18px;
    overflow: hidden;
    box-shadow: 0 14px 30px rgba(0,0,0,.5);
  }

  /* Front side */
  .card-front { left: 60px; top: 70px; background: var(--card-grey); }
  .card-front .brand {
    position: absolute; left: 0; right: 0; top: 130px;
    display: flex; align-items: center; justify-content: center; gap: 16px;
  }
  .brand-dot { width: 34px; height: 34px; border-radius: 50%; background: var(--green-bright); flex: none; }
  .card-front .brand-name {
    font-weight: 700; font-size: 44px; letter-spacing: 1px;
    color: var(--text-light); text-transform: uppercase;
  }
  .card-front .web {
    position: absolute; left: 0; right: 0; bottom: 44px;
    text-align: center; color: var(--text-light); font-size: 14px; font-weight: 500;
  }

  /* Back side */
  .card-back { left: 520px; top: 480px; background: var(--card-white); }
  .card-back .wave { position: absolute; inset: 0; }
  .card-back .brand {
    position: absolute; left: 34px; top: 104px;
    display: flex; align-items: center; gap: 10px;
  }
  .card-back .brand-dot { width: 24px; height: 24px; }
  .card-back .brand-name {
    font-weight: 700; font-size: 26px; letter-spacing: .5px;
    color: var(--text-dark); text-transform: uppercase;
  }
  .person { position: absolute; right: 40px; top: 24px; text-align: right; }
  .person-name { font-weight: 700; font-size: 18px; line-height: 1.2; color: var(--green-deep); text-transform: uppercase; }
  .person-role { font-weight: 600; font-size: 9px; line-height: 1.3; color: var(--green-bright); text-transform: uppercase; letter-spacing: .5px; }

  .contacts {
    position: absolute; right: 28px; top: 172px;
    list-style: none; display: flex; flex-direction: column; gap: 7px;
  }
  .contacts li {
    display: flex; align-items: center; justify-content: flex-end; gap: 10px;
    color: var(--text-light); font-size: 13px;
  }
  .contact-icon {
    width: 20px; height: 20px; background: var(--card-white); border-radius: 2px;
    display: flex; align-items: center; justify-content: center;
  }
  .contact-icon svg { width: 14px; height: 14px; }

  .address {
    position: absolute; left: 60px; bottom: 22px;
    color: var(--text-light); font-size: 13px; line-height: 1.35; font-weight: 500;
  }
</style>
</head>
<body>
<div class="canvas">

  <section class="card card-front">
    <div class="brand">
      <span class="brand-dot"></span>
      <span class="brand-name">Tolbrin Waste</span>
    </div>
    <p class="web">www.tolbrinwaste.com</p>
  </section>

  <section class="card card-back">
    <svg class="wave" viewBox="0 0 620 354" preserveAspectRatio="none" aria-hidden="true">
      <path d="M0,262 C180,262 280,232 360,160 C440,88 520,78 620,72 L620,354 L0,354 Z" fill="var(--green-bright)"/>
      <path d="M0,272 C180,272 285,242 364,172 C444,102 524,92 620,88 L620,354 L0,354 Z" fill="var(--green-deep)"/>
      <path d="M0,278 C182,278 288,248 366,180 C446,110 526,102 620,98 L620,354 L0,354 Z" fill="var(--card-white)"/>
      <path d="M0,284 C184,284 290,254 368,188 C448,118 528,110 620,108 L620,354 L0,354 Z" fill="var(--card-grey)"/>
    </svg>

    <div class="brand">
      <span class="brand-dot"></span>
      <span class="brand-name">Tolbrin Waste</span>
    </div>

    <div class="person">
      <p class="person-name">Rowan Hale</p>
      <p class="person-role">Owner</p>
    </div>

    <ul class="contacts">
      <li>555-018-2740
        <span class="contact-icon"><svg viewBox="0 0 24 24"><path fill="var(--green-deep)" d="M6.6 10.8a15 15 0 0 0 6.6 6.6l2.2-2.2c.3-.3.7-.4 1-.2 1.1.4 2.3.6 3.6.6.6 0 1 .4 1 1V20c0 .6-.4 1-1 1A17 17 0 0 1 3 4c0-.6.4-1 1-1h3.5c.6 0 1 .4 1 1 0 1.3.2 2.5.6 3.6.1.3 0 .7-.2 1z"/></svg></span>
      </li>
      <li>555-018-2741
        <span class="contact-icon"><svg viewBox="0 0 24 24"><rect x="3" y="10" width="18" height="11" rx="2" fill="var(--green-deep)"/><path d="M2 8c0-3 20-3 20 0v2h-5V8H7v2H2z" fill="var(--green-deep)"/></svg></span>
      </li>
      <li>rowan@tolbrinwaste.com
        <span class="contact-icon"><svg viewBox="0 0 24 24"><rect x="2" y="5" width="20" height="14" rx="1" fill="var(--green-deep)"/><path d="M2 6l10 7 10-7" stroke="#fff" stroke-width="1.6" fill="none"/></svg></span>
      </li>
      <li>www.tolbrinwaste.com
        <span class="contact-icon"><svg viewBox="0 0 24 24"><circle cx="12" cy="12" r="9" fill="none" stroke="var(--green-deep)" stroke-width="2"/><ellipse cx="12" cy="12" rx="4" ry="9" fill="none" stroke="var(--green-deep)" stroke-width="1.6"/><path d="M3 12h18" stroke="var(--green-deep)" stroke-width="1.6"/></svg></span>
      </li>
    </ul>

    <p class="address">Level 2 Marlow Plaza<br>Tenby Street, Suva, Fiji</p>
  </section>

</div>
</body>
</html>
```